Poster to advertise new mind coaching clinic

Create a single sided A4 colour poster using the text provided. Suggested image provided. You may want to suggest an alternative however images need to appeal to both male and female sports people.

Text:
One-to-one mind coaching
For recreational and competitive sports people
Learn the mental tools and techniques used by the top sports people to fulfil your potential

 Create well-formed and achievable goals
 Overcome limiting beliefs
 Accelerate mastery through modelling your heroes
 Learn how to use mental rehearsal to increase your chances of success
 Smash through belief ceilings
 Get into the zone to bring your best game more often
Thursdays in central Twyford
5-8pm
For more information contact:
stellvanementoring@quorvexmail.com
Tel: 07700 900482
www.stellvane-mind.co.uk

sports people

Clinic

• All the content provided. Contact details.

```html
<!DOCTYPE html>
<html lang="en">
<head>
<meta charset="utf-8">
<title>Stellvane – One-to-one Mind Coaching</title>
<link rel="stylesheet" href="https://fonts.googleapis.com/css2?family=Arimo:ital,wght@0,400;0,700;1,700&family=Roboto+Condensed:ital,wght@0,400;1,700&display=swap">
<style>
  :root {
    --page-bg: #e9e9e9;
    --sky: #4bbfea;
    --lavender: #98b3e0;
    --mist: #c9d6ef;
    --paper: #ffffff;
    --ink: #222222;
    --track-deep: #2f7fc8;
    --track-light: #5aa9e6;
  }
  * { margin: 0; padding: 0; box-sizing: border-box; }
  html, body { width: 1200px; height: 1200px; overflow: hidden; background: var(--page-bg); }
  .poster {
    position: absolute; left: 190px; top: 20px;
    width: 955px; height: 1350px;
    transform: scale(0.8593); transform-origin: 0 0;
    overflow: hidden; background: var(--sky);
    box-shadow: 0 4px 18px rgba(0,0,0,.25);
    font-family: "Arimo", Arial, sans-serif; color: var(--ink);
  }
  .poster-shapes { position: absolute; inset: 0; }
  .headline {
    position: absolute; left: 32px; top: 236px;
    font-size: 70px; font-weight: 700; line-height: 84px; letter-spacing: -0.5px;
  }
  .intro {
    position: absolute; left: 32px; top: 414px; width: 660px;
    font-size: 28px; line-height: 35px;
  }
  .benefits {
    position: absolute; left: 32px; top: 560px; width: 420px;
    list-style: none; font-family: "Roboto Condensed", "Arial Narrow", sans-serif;
    font-size: 23px; line-height: 29px;
  }
  .benefits li { position: relative; padding-left: 20px; margin-bottom: 8px; }
  .benefits li::before {
    content: ""; position: absolute; left: 2px; top: 12px;
    width: 7px; height: 7px; border-radius: 50%; background: var(--ink);
  }
  .contact {
    position: absolute; left: 32px; top: 906px;
    font-family: "Roboto Condensed", "Arial Narrow", sans-serif; font-size: 23px;
  }
  .contact p { line-height: 41px; }
  .contact .contact-title { font-family: "Arimo", Arial, sans-serif; font-style: italic; font-weight: 700; font-size: 23px; }
  .brand {
    position: absolute; left: 575px; top: 20px; width: 370px; height: 370px;
    display: flex; align-items: center; justify-content: center; gap: 14px;
  }
  .brand-dot { width: 34px; height: 34px; border-radius: 50%; background: var(--sky); }
  .brand-name { font-size: 48px; font-weight: 700; color: var(--ink); }
  .schedule {
    position: absolute; left: 635px; top: 540px; width: 310px; height: 310px;
    display: flex; flex-direction: column; align-items: center; justify-content: center;
    font-size: 38px; line-height: 50px; text-align: center;
  }
  .schedule strong { font-weight: 700; }
</style>
</head>
<body>
<main class="poster">
  <svg class="poster-shapes" viewBox="0 0 955 1350" width="955" height="1350">
    <defs>
      <linearGradient id="panelFade" x1="0" y1="0" x2="0" y2="1">
        <stop offset="0" stop-color="var(--lavender)"/>
        <stop offset="0.55" stop-color="var(--mist)"/>
        <stop offset="1" stop-color="var(--paper)"/>
      </linearGradient>
      <linearGradient id="trackTone" x1="0" y1="0" x2="1" y2="1">
        <stop offset="0" stop-color="var(--track-light)"/>
        <stop offset="1" stop-color="var(--track-deep)"/>
      </linearGradient>
      <filter id="softShadow" x="-20%" y="-20%" width="140%" height="140%">
        <feDropShadow dx="0" dy="4" stdDeviation="6" flood-color="#000" flood-opacity="0.25"/>
      </filter>
    </defs>
    <path class="content-panel" fill="url(#panelFade)"
      d="M0,235 C150,110 330,72 520,82 C700,95 890,240 955,362 L955,788 C700,790 480,950 385,1100 C300,1235 150,1330 0,1345 Z"/>
    <circle cx="677" cy="1135" r="287" fill="url(#trackTone)" role="img"
      aria-label="Photo of a sprinter crossing the finish line with arms raised on a blue track"/>
    <circle cx="760" cy="205" r="185" fill="var(--paper)" filter="url(#softShadow)"/>
    <circle cx="790" cy="695" r="155" fill="var(--paper)" filter="url(#softShadow)"/>
  </svg>

  <div class="brand">
    <span class="brand-dot"></span>
    <span class="brand-name">Stellvane</span>
  </div>

  <h1 class="headline">One-to-one<br>Mind Coaching</h1>

  <p class="intro">For recreational and competitive sports people<br>Learn the mental tools and techniques used by<br>the top sports people to fulfil your potential</p>

  <ul class="benefits">
    <li>Create well-formed and achievable goals</li>
    <li>Overcome limiting beliefs</li>
    <li>Accelerate mastery through modelling your heroes</li>
    <li>Learn how to use mental rehearsal to increase your chances of success</li>
    <li>Smash through belief ceilings</li>
    <li>Get into the zone to bring your best game more often</li>
  </ul>

  <div class="contact">
    <p class="contact-title">For more information contact:</p>
    <p>Tel: 07700 900482</p>
    <p>stellvanementoring@quorvexmail.com</p>
    <p>www.stellvane-mind.co.uk</p>
  </div>

  <div class="schedule">
    <strong>Thursdays</strong>
    <span>in central</span>
    <span>Twyford</span>
    <strong>at 5-8pm</strong>
  </div>
</main>
</body>
</html>
```